Creative Businesss Card desgin!

Create a business card for our business Gleam window cleaning!
We are open to creative ideas as long as it maintains a professional image.

Target Market(s)

Small Commercial window cleaning clients including car dealerships, strata manager, cafe

Industry/Entity Type

Window Cleaning

Contact Information for Business Card

Daniel Prescott
General Manager
Gleam Window Cleaning

daniel@gleamservices.com.au
pane-care-southbank.com.au
Ph: 1800 GET GLEAM
Mob: 0437 582 061

Colors
fbed22
0392cd

Requirements
Should not have
• Stock window cleaning/ squeegee graphics

```html
<!DOCTYPE html>
<html lang="en">
<head>
<meta charset="utf-8">
<title>Gleam Window Cleaning – Business Card</title>
<link href="https://fonts.googleapis.com/css2?family=Oswald:wght@600&family=Work+Sans:wght@400;500;700&display=swap" rel="stylesheet">
<style>
  :root {
    --stage: #2b2d30;
    --card-white: #ffffff;
    --card-shade: #ececec;
    --brand-blue: #0d5288;
    --brand-blue-deep: #0a3f6b;
    --brand-blue-light: #0f5f98;
    --brand-yellow: #c9c71c;
    --text-grey: #4a4a4a;
    --text-soft: #d5dde6;
    --rule: #2d6fa3;
  }
  * { margin: 0; padding: 0; box-sizing: border-box; }
  html, body {
    width: 1200px; height: 900px; overflow: hidden;
    background: var(--stage);
  }
  .stage {
    width: 1200px; height: 900px;
    display: flex; flex-direction: column;
    align-items: center; justify-content: center; gap: 40px;
  }
  .card {
    width: 640px; height: 391px;
    position: relative; overflow: hidden;
    box-shadow: 0 12px 30px rgba(0,0,0,0.45);
  }
  /* Front */
  .card-front {
    background: linear-gradient(135deg, var(--card-shade) 0%, var(--card-white) 45%, var(--card-white) 100%);
    display: flex; align-items: center;
    padding-left: 70px;
  }
  .identity { text-align: right; width: 230px; }
  .person-name {
    font-family: "Oswald", sans-serif; font-weight: 600;
    font-size: 32px; letter-spacing: 0.5px; line-height: 1;
    color: var(--brand-blue); text-transform: uppercase;
  }
  .person-role {
    font-family: "Work Sans", sans-serif; font-size: 15px;
    color: var(--text-grey); margin-top: 8px;
  }
  .divider {
    width: 2px; height: 86px; background: var(--rule);
    margin: 30px 0 0 26px; align-self: center;
  }
  .contacts { list-style: none; margin: 70px 0 0 22px; }
  .contact {
    font-family: "Work Sans", sans-serif; font-size: 15.5px;
    color: var(--text-grey); line-height: 21px;
    display: flex; align-items: center; gap: 9px;
  }
  .contact svg { width: 11px; height: 11px; flex: none; fill: var(--brand-blue-light); }
  /* Back */
  .card-back {
    background: linear-gradient(160deg, var(--brand-blue-light) 0%, var(--brand-blue) 50%, var(--brand-blue-deep) 100%);
    display: flex; flex-direction: column;
    align-items: center; justify-content: center;
  }
  .brand-name {
    font-family: "Work Sans", sans-serif; font-weight: 700;
    color: var(--brand-yellow); text-transform: uppercase;
    text-align: center; line-height: 1.05;
  }
  .brand-name .brand-main { display: block; font-size: 78px; letter-spacing: 4px; }
  .brand-name .brand-sub { display: block; font-size: 30px; letter-spacing: 3px; }
  .brand-web {
    font-family: "Work Sans", sans-serif; font-size: 17px;
    color: var(--text-soft); margin-top: 34px; letter-spacing: 0.5px;
  }
</style>
</head>
<body>
<main class="stage">
  <section class="card card-front">
    <div class="identity">
      <h1 class="person-name">Daniel Prescott</h1>
      <p class="person-role">General Manager</p>
    </div>
    <div class="divider"></div>
    <ul class="contacts">
      <li class="contact">
        <svg viewBox="0 0 12 12" aria-hidden="true"><path d="M2.5 1 4.5 1 5 3.5 3.8 4.4C4.4 5.8 5.5 7 7 7.7L8 6.5 10.5 7.2 10.5 9.3C10.5 10 9.9 10.6 9.2 10.5 4.9 10 1.6 6.8 1.3 2.4 1.3 1.6 1.8 1 2.5 1Z"/></svg>
        1800 GET GLEAM
      </li>
      <li class="contact">
        <svg viewBox="0 0 12 12" aria-hidden="true"><path d="M3.5 0.5h5a1 1 0 0 1 1 1v9a1 1 0 0 1-1 1h-5a1 1 0 0 1-1-1v-9a1 1 0 0 1 1-1Zm0.5 1.5v6.5h4V2Z"/></svg>
        0437 582 061
      </li>
      <li class="contact">
        <svg viewBox="0 0 12 12" aria-hidden="true"><path d="M1 2.5h10v7H1Zm1 1v0.3l4 2.7 4-2.7V3.5Zm0 1.5v3.5h8V5L6 7.7Z"/></svg>
        daniel@gleamservices.com.au
      </li>
      <li class="contact">
        <svg viewBox="0 0 12 12" aria-hidden="true"><path d="M6 0.8a5.2 5.2 0 1 0 0 10.4A5.2 5.2 0 0 0 6 0.8Zm-3.9 4.7h1.8c0-1.3.3-2.5.8-3.3A4.2 4.2 0 0 0 2.1 5.5Zm2.8 0h2.2C7 4 6.6 2.7 6 2 5.4 2.7 5 4 4.9 5.5Zm3.2 0h1.8a4.2 4.2 0 0 0-2.6-3.3c.5.8.8 2 .8 3.3ZM2.1 6.5a4.2 4.2 0 0 0 2.6 3.3c-.5-.8-.8-2-.8-3.3Zm2.8 0C5 8 5.4 9.3 6 10c.6-.7 1-2 1.1-3.5Zm3.2 0c0 1.3-.3 2.5-.8 3.3a4.2 4.2 0 0 0 2.6-3.3Z"/></svg>
        pane-care-southbank.com.au
      </li>
    </ul>
  </section>

  <section class="card card-back">
    <h2 class="brand-name">
      <span class="brand-main">Gleam</span>
      <span class="brand-sub">Window Cleaning</span>
    </h2>
    <p class="brand-web">pane-care-southbank.com.au</p>
  </section>
</main>
</body>
</html>
```